High-end construction company needs a business card design

We need a modern looking business card that draws people in, is memorable and looks so good people will want to sick it on their fridges.
On the first side what is needed are:
Logo
My name - Tomas Verbelk
Title - Managing Director
Website - www.kravel.co.uk
Email - tomas@kravel.co.uk
Telephone - 020 5194 6381
Mobile - 07845319027
On the back side was is needed is a list of all the services we provide:
-Kitchen Renovations
-Bathroom Renovations
-House Renovations
-Garage Conversions
-Extensions
-Loft Conversions
-Conservatories
-Carpentry
-Tiling
-Electrical
-Plumbing & Heating
-Bricklaying
-Landscaping
-Decorating
-Plastering
We would like the colours to be the same shades as on the logo with grey or black for the words.
Target Market(s)
Anyone who needs building work done
Contact Information for Business Card
This business card is for a construction company which strives to deliver excellent service and quality.
The look and feel of the card should represent this.
Requirements
Must have
- On the first side what is needed are:
Logo
My name - Tomas Verbelk
Title - Managing Director
Website - www.kravel.co.uk
Email - tomas@kravel.co.uk
Telephone - 020 5194 6381
Mobile - 07845319027
Nice to have
- Cool looking features

```html
<!DOCTYPE html>
<html lang="en">
<head>
<meta charset="utf-8">
<title>Kravel Construction Ltd – Business Card</title>
<link href="https://fonts.googleapis.com/css2?family=Oxanium:wght@400;500;600&display=swap" rel="stylesheet">
<style>
  :root {
    --backdrop: #1c1c1e;
    --card: #363638;
    --text: #d6d6d8;
    --text-soft: #bdbdc0;
    --rule: #a9a9ad;
    --brand-green: #5cb83a;
  }
  * { box-sizing: border-box; margin: 0; padding: 0; }
  html, body {
    width: 1200px; height: 900px; overflow: hidden;
    background: var(--backdrop);
    font-family: "Oxanium", sans-serif;
  }
  .sheet {
    width: 1200px; height: 900px;
    display: flex; flex-direction: column; align-items: center; justify-content: center;
    gap: 30px;
  }
  .card {
    position: relative;
    width: 720px; height: 411px;
    background: var(--card);
    border-radius: 4px;
    box-shadow: 0 10px 28px rgba(0,0,0,.45);
    color: var(--text);
    overflow: hidden;
  }

  /* Front */
  .holder { position: absolute; left: 48px; top: 60px; }
  .holder-name { font-size: 32px; font-weight: 500; letter-spacing: 1.5px; }
  .holder-title { font-size: 17px; letter-spacing: 2px; margin-top: 4px; color: var(--text-soft); }
  .brand {
    position: absolute; right: 52px; top: 70px;
    display: flex; align-items: center; gap: 14px;
  }
  .brand-dot { width: 22px; height: 22px; border-radius: 50%; background: var(--brand-green); }
  .brand-name {
    color: var(--brand-green); font-weight: 600; font-size: 30px; letter-spacing: 2px;
    text-transform: uppercase; line-height: 1.1;
  }
  .brand-name small { display: block; font-size: 14px; letter-spacing: 4px; }
  .phones, .online {
    position: absolute; bottom: 56px;
    font-size: 18px; letter-spacing: 1.5px; line-height: 1.7;
  }
  .phones { left: 48px; }
  .online { right: 52px; text-align: left; }

  /* Back */
  .services-heading {
    position: absolute; left: 48px; top: 56px;
    font-size: 22px; letter-spacing: 1.5px;
  }
  .rule { position: absolute; height: 1.5px; background: var(--rule); }
  .rule-heading { left: 100px; top: 92px; width: 170px; }
  .rule-column { left: 420px; top: 56px; width: 90px; }
  .service-list {
    position: absolute; list-style: none;
    font-size: 19px; letter-spacing: 1.2px; line-height: 1.58;
  }
  .service-list.col-a { left: 100px; top: 102px; }
  .service-list.col-b { left: 420px; top: 66px; }
  .rule-foot-left { left: 100px; bottom: 48px; width: 390px; }
  .rule-foot-right { right: 48px; bottom: 48px; width: 120px; }
  .foot-brand {
    position: absolute; right: 180px; bottom: 38px;
    color: var(--brand-green); font-weight: 600; font-size: 16px; letter-spacing: 2px;
    text-transform: uppercase;
  }
</style>
</head>
<body>
<main class="sheet">

  <section class="card card-front" aria-label="Business card front">
    <div class="holder">
      <h1 class="holder-name">Tomas Verbelk</h1>
      <p class="holder-title">Managing Director</p>
    </div>
    <div class="brand">
      <span class="brand-dot"></span>
      <p class="brand-name">Kravel<small>Construction Ltd</small></p>
    </div>
    <div class="phones">
      <p>020 5194 6381</p>
      <p>07845 319027</p>
    </div>
    <div class="online">
      <p>www.kravel.co.uk</p>
      <p>tomas@kravel.co.uk</p>
    </div>
  </section>

  <section class="card card-back" aria-label="Business card back">
    <h2 class="services-heading">Services</h2>
    <span class="rule rule-heading"></span>
    <ul class="service-list col-a">
      <li>Kitchen Renovations</li>
      <li>Bathroom Renovations</li>
      <li>House Renovations</li>
      <li>Garage Conversions</li>
      <li>Extensions</li>
      <li>Loft Conversions</li>
      <li>Conservatories</li>
      <li>Carpentry</li>
    </ul>
    <span class="rule rule-column"></span>
    <ul class="service-list col-b">
      <li>Tiling</li>
      <li>Electrical</li>
      <li>Plumbing &amp; Heating</li>
      <li>Bricklaying</li>
      <li>Landscaping</li>
      <li>Decorating</li>
      <li>Plastering</li>
    </ul>
    <span class="rule rule-foot-left"></span>
    <p class="foot-brand">Kravel</p>
    <span class="rule rule-foot-right"></span>
  </section>

</main>
</body>
</html>
```